Lanterns Over The Quiet Meadow Waters Book Cover

Book cover for a new book titled "Lanterns Over The Quiet Meadow Waters" which will show how retirees can pay NO tax in their retirement. Would like you to use your creative inspiration to come up with a design.

Please make MEADOW WATERS the emphasis of the title.

can you show money being rescued, or freed, from taxes.

I'm trying convey the message that retirees can FREE themselves from the burden of taxes in retirement by reading this book and following the instructions. Think about a person swimming with a weight on his back, sinking him. Suddenly the weight is removed. The feeling and imagery of the load being light now

Doing MEADOW WATERS can alleviate many of unnecessary taxes which will weight retirees down. But, unfortunately, many advisors in my industry do not educate their clients on this stuff.

Not a fan of dark backgrounds, generally speaking. Lighter is good.

Remember folks, go to brindlecart. Type in Roth IRA books. what will jump out over the stuff that's already there? Thanks!

Target Market(s)

recent, or soon to be, retirees, people in their 50s and 60s, typically couples

Industry/Entity Type

Financial

Font styles to use
Serif

Colors

Designer to choose colors to be used in the design.

Requirements
Must have
• Be optimistic, sunny, happy. How you do that? I don't know, that's why I'm hiring you. This book is designed for the lay person, (average Joe and Jane)
• Put my picture on the lower back.
• My name at bottom of the cover
Nice to have
• Be nice to have the cover POP on Brindlecart because I'm competing with so many other books and thumbnails
• Maybe a kite with a dollar bill that is breaking from a ball and chain? Just an idea.
Should not have
• No guys in suits. Happy couples sitting on the beach or sailing. That stuff is in every piece of financial planning literature.
• NOT TECHNICAL. NO PIGGY BANKS Design please

```html
<!DOCTYPE html>
<html lang="en">
<head>
<meta charset="utf-8">
<title>Lanterns Over The Quiet Meadow Waters — Book Cover</title>
<link href="https://fonts.googleapis.com/css2?family=Cinzel:wght@400;500;600&family=Cormorant+Garamond:wght@500&display=swap" rel="stylesheet">
<style>
  :root {
    --backdrop: #ece9e2;
    --paper: #f1f1f1;
    --paper-edge: #dcdcdc;
    --title-navy: #0f2f6e;
    --band-green: #6aae16;
    --band-white: #ffffff;
    --author-teal: #5ea8ab;
    --url-ink: #222222;
    --bill-light: #cfcfc8;
    --bill-dark: #7c7f78;
  }
  html, body {
    margin: 0;
    width: 1200px;
    height: 800px;
    overflow: hidden;
    background: var(--backdrop);
  }
  .canvas {
    position: relative;
    width: 1200px;
    height: 800px;
  }
  .cover {
    position: absolute;
    left: 350px;
    top: 18px;
    width: 500px;
    height: 764px;
    background: linear-gradient(180deg, #fafafa 0%, var(--paper) 60%, #e9e9e9 100%);
    border-radius: 3px;
    overflow: hidden;
  }
  .title-lead {
    position: absolute;
    top: 88px;
    left: 0;
    right: 0;
    margin: 0;
    text-align: center;
    font-family: "Cinzel", serif;
    font-weight: 600;
    font-size: 46px;
    line-height: 62px;
    color: var(--title-navy);
    white-space: nowrap;
  }
  .title-lead span { display: block; }
  .band {
    position: absolute;
    left: 0;
    top: 200px;
    width: 500px;
    height: 200px;
  }
  .band svg { display: block; }
  .title-emphasis {
    position: absolute;
    top: 236px;
    left: 0;
    right: 0;
    margin: 0;
    text-align: center;
    font-family: "Cinzel", serif;
    font-weight: 400;
    color: var(--band-white);
    white-space: nowrap;
  }
  .title-emphasis span {
    display: block;
    font-size: 64px;
    line-height: 64px;
  }
  .artwork {
    position: absolute;
    left: 80px;
    top: 402px;
    width: 330px;
    height: 252px;
  }
  .author {
    position: absolute;
    top: 676px;
    left: 0;
    right: 0;
    margin: 0;
    text-align: center;
    font-family: "Cinzel", serif;
    font-weight: 400;
    font-size: 42px;
    line-height: 48px;
    letter-spacing: 3px;
    color: var(--author-teal);
    white-space: nowrap;
  }
  .website {
    position: absolute;
    top: 727px;
    left: 0;
    right: 0;
    margin: 0;
    text-align: center;
    font-family: "Cormorant Garamond", serif;
    font-weight: 500;
    font-size: 15px;
    letter-spacing: 2.6px;
    color: var(--url-ink);
    white-space: nowrap;
  }
</style>
</head>
<body>
<main class="canvas">
  <article class="cover">
    <h1 class="title-lead">
      <span>Lanterns Over</span>
      <span>The Quiet</span>
    </h1>

    <div class="band">
      <svg width="500" height="200" viewBox="0 0 500 200" aria-hidden="true">
        <polygon class="torn-paper-top" fill="#ffffff"
          points="0,6 40,4 90,8 140,3 200,9 260,5 320,10 380,6 440,9 500,5 500,24 0,22"/>
        <polygon class="green-band" fill="var(--band-green)"
          points="0,22 30,20 60,24 95,19 130,23 170,18 210,22 250,17 290,21 330,18 370,23 410,19 450,22 500,20
                  500,183 470,185 430,181 390,186 350,182 310,187 270,183 230,188 190,184 150,189 110,185 70,190 40,186 0,188"/>
        <polygon class="torn-paper-bottom" fill="#ffffff"
          points="0,188 40,186 70,190 110,185 150,189 190,184 230,188 270,183 310,187 350,182 390,186 430,181 470,185 500,183
                  500,198 0,200"/>
        <polygon class="paper-curl" fill="var(--paper-edge)" points="0,188 22,190 12,200 0,205"/>
      </svg>
    </div>

    <h2 class="title-emphasis">
      <span>Meadow</span>
      <span>Waters</span>
    </h2>

    <svg class="artwork" viewBox="0 0 330 252" role="img" aria-label="Photograph of a dollar bill folded into an origami butterfly">
      <defs>
        <linearGradient id="bill-tone" x1="0" y1="0" x2="1" y2="1">
          <stop offset="0%" stop-color="var(--bill-light)"/>
          <stop offset="100%" stop-color="var(--bill-dark)"/>
        </linearGradient>
      </defs>
      <rect x="0" y="0" width="330" height="252" rx="8" fill="url(#bill-tone)" opacity="0.55"/>
    </svg>

    <p class="author">Evan Marlowe</p>
    <p class="website">www.fairbrookplanning.com</p>
  </article>
</main>
</body>
</html>
```